Redesign of Smart Watch Gift Voucher-SEE ATTACHED CURRENT DESIGN

I need to redesign my existing design using all same content and elements.

MY ENVISION: I invision more of a professional advertisement type of flyer/voucher. Imagine how Corvel.com would create a professionally looking flyer promoting the lumo or veno.

you can get many ideas about professional design by looking at some of corvels flyer designs :
https://www.findora-example.net/search?q=lumo+advertisment&mode=img&ref=a83kd02mzq7

stock photos are attached, you do not have to use them all, you can use some or none i am open to your designs using your own images if you want...just make sure the smartwatch looks black

DO NOT LEAVE ANY CONTENT OR ELEMENTS OUT ON MOCK UP PLEASE

SEE ATTACHED CURRENT DESIGN

I need to redesign my existing design using all same content and elements. DO NOT LEAVE ANY CONTENT OR ELEMENTS OUT ON MOCK UP PLEASE

Target Market(s)

B2B-you can get many ideas about professional design by looking at some of corvels flyer designs :

Industry/Entity Type

Marketing

Requirements
Must have
• I need to redesign my existing design using all same content and elements. DO NOT LEAVE ANY CONTENT OR ELEMENTS OUT ON MOCK UP PLEASE

Nice to have

Should not have

```html
<!DOCTYPE html>
<html lang="en">
<head>
<meta charset="utf-8">
<title>Smartwatch Reward Voucher</title>
<link rel="stylesheet" href="https://fonts.googleapis.com/css2?family=Montserrat:ital,wght@0,400;0,600;0,700;0,800;0,900;1,700;1,800;1,900&family=Oswald:wght@600;700&display=swap">
<style>
  :root {
    --red: #d21d1d;
    --red-deep: #c10f0f;
    --yellow: #f4e400;
    --ink: #1b1b1b;
    --charcoal: #2a2a2a;
    --grey-line: #c6c6c6;
    --paper: #ffffff;
    --page: #e6e6e6;
    --body-text: #3a3a3a;
  }
  * { box-sizing: border-box; margin: 0; padding: 0; }
  html, body { width: 1200px; height: 2295px; overflow: hidden; background: var(--page); }
  body { position: relative; font-family: "Montserrat", Arial, sans-serif; }

  .flyer {
    position: absolute; left: 50px; top: 436px; width: 1100px; height: 1424px;
    background: var(--paper); overflow: hidden;
    box-shadow: 0 10px 28px rgba(0,0,0,.25);
  }
  .abs { position: absolute; }
  .nowrap { white-space: nowrap; }

  /* header */
  .header { left: 0; top: 0; width: 1100px; height: 212px; }
  .title-enjoy {
    left: 104px; top: 40px; font-size: 108px; font-weight: 900; letter-spacing: -3px; line-height: 1;
    background: linear-gradient(180deg, #ffffff 0%, #e6e6e6 40%, #9a9a9a 55%, #f2f2f2 80%, #bdbdbd 100%);
    -webkit-background-clip: text; background-clip: text; color: transparent;
  }
  .title-right { left: 537px; top: 44px; font-weight: 900; font-size: 45px; line-height: 1; }
  .title-right .line-yellow { color: var(--yellow); }
  .title-right .line-white { color: var(--paper); margin-top: 4px; }

  /* photo area */
  .hero-photo { left: 0; top: 0; width: 1100px; height: 757px; }
  .inset-photo {
    left: 71px; top: 210px; width: 330px; height: 330px; border-radius: 50%;
    background: radial-gradient(circle at 45% 40%, #d9c3b0 0%, #9a8a80 35%, #3b4250 70%, #1c2230 100%);
    border: 5px solid #4a4a4a;
  }
  .hero-headline {
    left: 106px; top: 555px; font-weight: 900; font-style: italic; font-size: 44px; line-height: 46px;
    letter-spacing: -.5px; white-space: nowrap;
  }
  .hero-headline .white { color: var(--paper); }
  .hero-headline .yellow { color: var(--yellow); }

  /* certificate */
  .certificate-shape { left: 0; top: 660px; width: 1100px; height: 280px; }
  .certificate-text { left: 630px; width: 410px; text-align: center; white-space: nowrap; }
  .certificate-label { top: 708px; color: var(--yellow); font-weight: 800; font-size: 38px; line-height: 1; letter-spacing: .5px; }
  .certificate-number { top: 748px; font-family: "Oswald", "Arial Narrow", sans-serif; font-weight: 700; color: var(--paper); font-size: 72px; line-height: 1; letter-spacing: -2px; }
  .certificate-expiry { top: 832px; font-family: "Oswald", "Arial Narrow", sans-serif; font-weight: 700; color: var(--yellow); font-size: 40px; line-height: 1; letter-spacing: -.5px; }

  /* body copy */
  .intro { left: 116px; top: 788px; font-size: 17px; line-height: 21.6px; color: var(--body-text); white-space: nowrap; }

  .features-band { left: 109px; top: 1007px; width: 440px; height: 90px; }
  .features-title {
    left: 125px; top: 1018px; font-weight: 900; font-style: italic; font-size: 63px; line-height: 70px;
    color: var(--red); letter-spacing: -1px; white-space: nowrap;
  }
  .feature-list { list-style: none; font-weight: 700; font-size: 14px; color: var(--ink); white-space: nowrap; }
  .feature-list li { height: 28.6px; display: flex; align-items: center; gap: 12px; }
  .feature-list svg { flex: none; }
  .features-left { left: 109px; top: 1115px; }
  .features-right { left: 322px; top: 1111px; }

  .section-title { font-weight: 900; font-style: italic; line-height: 1; color: var(--ink); white-space: nowrap; }
  .section-title em { color: var(--red); font-style: italic; }
  .others-title { left: 596px; top: 952px; font-size: 32px; }
  .quote { left: 594px; top: 1020px; width: 450px; font-size: 13.5px; line-height: 17px; color: var(--body-text); padding-left: 40px; white-space: nowrap; }
  .quote .mark { position: absolute; font-family: Georgia, serif; font-weight: 900; font-size: 46px; line-height: 1; color: var(--ink); }
  .quote .open { left: 0; top: -6px; }
  .quote .close { left: 352px; top: 10px; }
  .quote cite { display: block; font-weight: 800; font-style: italic; color: var(--ink); }
  .how-title { left: 601px; top: 1091px; font-size: 29px; }
  .how-copy { left: 601px; top: 1133px; font-size: 14px; line-height: 17.2px; color: var(--body-text); white-space: nowrap; }
  .how-copy b { color: var(--ink); }

  /* footer */
  .footer-shapes { left: 0; top: 1310px; width: 1100px; height: 114px; }
  .footer-cta { left: 118px; top: 1336px; color: var(--paper); font-weight: 800; font-size: 17px; line-height: 21px; white-space: nowrap; }
  .footer-cta .yellow { color: var(--yellow); font-weight: 400; }
  .footer-link { left: 467px; top: 1338px; white-space: nowrap; }
  .footer-url { color: var(--red); font-weight: 800; font-size: 26px; line-height: 1; letter-spacing: .5px; }
  .footer-terms { color: var(--ink); font-weight: 700; font-size: 19.5px; line-height: 1.3; margin-top: 3px; }
</style>
</head>
<body>
<main class="flyer">

  <svg class="abs hero-photo" viewBox="0 0 1100 757" role="img" aria-label="Photo of a runner in a blue shirt seated on stone steps, checking a black smartwatch and phone, with blue fitness feature icons">
    <defs>
      <linearGradient id="steps" x1="0" y1="0" x2="1" y2="1">
        <stop offset="0" stop-color="#cfc7bd"/>
        <stop offset=".5" stop-color="#e4ded6"/>
        <stop offset="1" stop-color="#b9b1a8"/>
      </linearGradient>
      <linearGradient id="shade" x1="0" y1="0" x2="1" y2="0">
        <stop offset="0" stop-color="#5e5b58"/>
        <stop offset=".4" stop-color="#6f6c69" stop-opacity=".85"/>
        <stop offset=".7" stop-color="#8a8784" stop-opacity="0"/>
      </linearGradient>
      <linearGradient id="darkfade" x1="0" y1="0" x2="0" y2="1">
        <stop offset="0" stop-color="#9a9794" stop-opacity="0"/>
        <stop offset=".55" stop-color="#55524f" stop-opacity=".9"/>
        <stop offset="1" stop-color="#3f3c3a"/>
      </linearGradient>
    </defs>
    <rect x="0" y="160" width="1100" height="597" fill="url(#steps)"/>
    <ellipse cx="640" cy="340" rx="190" ry="170" fill="#2e6fd6" opacity=".45"/>
    <rect x="0" y="160" width="1100" height="597" fill="url(#shade)"/>
    <polygon points="0,420 720,420 660,757 0,757" fill="url(#darkfade)"/>
    <polygon points="0,716 40,757 0,757" fill="var(--paper)"/>
    <polygon points="605,757 674,675 1100,675 1100,757" fill="var(--paper)"/>
  </svg>

  <svg class="abs header" viewBox="0 0 1100 212" aria-hidden="true">
    <polygon points="0,0 1100,0 1100,163 481,163 431,200 0,200" fill="var(--red)"/>
    <polygon points="0,200 431,200 481,163 1100,163 1100,172 487,172 437,209 0,209" fill="var(--grey-line)"/>
  </svg>
  <div class="abs title-enjoy">ENJOY</div>
  <div class="abs title-right">
    <div class="line-yellow">YOUR BRAND NEW</div>
    <div class="line-white">SMARTWATCH</div>
  </div>

  <div class="abs inset-photo" role="img" aria-label="Close-up photo of a wrist wearing a black smartwatch"></div>

  <div class="abs hero-headline">
    <div class="white">TALE CONTREAL</div>
    <div class="white">OR YOUR TE WHITIN</div>
    <div class="yellow">YOUR NEW SMART</div>
    <div class="yellow">LITIHNESS WATELN</div>
  </div>

  <svg class="abs certificate-shape" viewBox="0 660 1100 280" aria-hidden="true">
    <polygon points="605,757 674,675 690,675 621,757" fill="var(--grey-line)"/>
    <polygon points="525,778 661,919 1100,919 1100,930 655,930 515,782" fill="var(--grey-line)"/>
    <polygon points="674,675 1100,675 1100,919 661,919 525,778 605,757" fill="var(--red-deep)"/>
    <polygon points="674,675 1100,675 1100,690 662,690" fill="var(--red)"/>
  </svg>

  <div class="abs certificate-text certificate-label">CERTIFICATE ID</div>
  <div class="abs certificate-text certificate-number">91772-89218</div>
  <div class="abs certificate-text certificate-expiry">Expires 10/03/2020</div>

  <p class="abs intro">Congratulations, you have been rewarded<br>with a Brand New Smart Fitness Watch shipped<br>right to your door. Just pay shipping and handling.<br>Your new Smart Fitness Watch has these features:<br>sport mode, pedometer, distance, calorie, heart rate,<br>blood pressure, stopwatch, sleep monitoring, phone<br>locator, reminders, remote camera, an alarm clock<br>and much more!</p>

  <svg class="abs features-band" viewBox="0 0 440 90" aria-hidden="true">
    <polygon points="0,0 372,0 432,88 0,88" fill="var(--ink)"/>
    <polygon points="380,0 392,0 440,90 428,90" fill="#9a9a9a"/>
  </svg>
  <div class="abs features-title">FEATURES</div>

  <ul class="abs feature-list features-left">
    <li><svg width="18" height="18" viewBox="0 0 18 18"><circle cx="9" cy="9" r="9" fill="var(--red)"/><path d="M4.5 9.3l3 3 6-6.4" stroke="#fff" stroke-width="2.2" fill="none"/></svg>Pedometer</li>
    <li><svg width="18" height="18" viewBox="0 0 18 18"><circle cx="9" cy="9" r="9" fill="var(--red)"/><path d="M4.5 9.3l3 3 6-6.4" stroke="#fff" stroke-width="2.2" fill="none"/></svg>Calorie Counter</li>
    <li><svg width="18" height="18" viewBox="0 0 18 18"><circle cx="9" cy="9" r="9" fill="var(--red)"/><path d="M4.5 9.3l3 3 6-6.4" stroke="#fff" stroke-width="2.2" fill="none"/></svg>Blood Pressure Monitor</li>
    <li><svg width="18" height="18" viewBox="0 0 18 18"><circle cx="9" cy="9" r="9" fill="var(--red)"/><path d="M4.5 9.3l3 3 6-6.4" stroke="#fff" stroke-width="2.2" fill="none"/></svg>Sleep Monitoring</li>
    <li><svg width="18" height="18" viewBox="0 0 18 18"><circle cx="9" cy="9" r="9" fill="var(--red)"/><path d="M4.5 9.3l3 3 6-6.4" stroke="#fff" stroke-width="2.2" fill="none"/></svg>Reminders Feature</li>
    <li><svg width="18" height="18" viewBox="0 0 18 18"><circle cx="9" cy="9" r="9" fill="var(--red)"/><path d="M4.5 9.3l3 3 6-6.4" stroke="#fff" stroke-width="2.2" fill="none"/></svg>Alarm Clock</li>
  </ul>
  <ul class="abs feature-list features-right">
    <li><svg width="18" height="18" viewBox="0 0 18 18"><circle cx="9" cy="9" r="9" fill="var(--red)"/><path d="M4.5 9.3l3 3 6-6.4" stroke="#fff" stroke-width="2.2" fill="none"/></svg>Distance Tracker</li>
    <li><svg width="18" height="18" viewBox="0 0 18 18"><circle cx="9" cy="9" r="9" fill="var(--red)"/><path d="M4.5 9.3l3 3 6-6.4" stroke="#fff" stroke-width="2.2" fill="none"/></svg>Heart Rate Monitor</li>
    <li><svg width="18" height="18" viewBox="0 0 18 18"><circle cx="9" cy="9" r="9" fill="var(--red)"/><path d="M4.5 9.3l3 3 6-6.4" stroke="#fff" stroke-width="2.2" fill="none"/></svg>Stopwatch</li>
    <li><svg width="18" height="18" viewBox="0 0 18 18"><circle cx="9" cy="9" r="9" fill="var(--red)"/><path d="M4.5 9.3l3 3 6-6.4" stroke="#fff" stroke-width="2.2" fill="none"/></svg>Phone Locator</li>
    <li><svg width="18" height="18" viewBox="0 0 18 18"><circle cx="9" cy="9" r="9" fill="var(--red)"/><path d="M4.5 9.3l3 3 6-6.4" stroke="#fff" stroke-width="2.2" fill="none"/></svg>Remote Camera</li>
    <li><svg width="18" height="18" viewBox="0 0 18 18"><circle cx="9" cy="9" r="9" fill="var(--red)"/><path d="M4.5 9.3l3 3 6-6.4" stroke="#fff" stroke-width="2.2" fill="none"/></svg>Waterproof</li>
  </ul>

  <h2 class="abs section-title others-title">WHAT <em>OTHERS SAY</em></h2>
  <blockquote class="abs quote">
    <span class="mark open">&ldquo;</span>
    Are you sure this is not a Nexora Orbit<br>Smartwatch in&nbsp; DISGUISE???? &nbsp;I love mine.
    <cite>-Dale M. Atlantic City, NJ</cite>
    <span class="mark close">&rdquo;</span>
  </blockquote>

  <h2 class="abs section-title how-title">HOW CAN <em>WE DO THIS?</em></h2>
  <p class="abs how-copy">We have a couple retail partners that we team up with<br>to "crowd purchase" huge shipping containers that<br>hold 10's of thousands of electronic products at<br><b>80-90% off</b> retail. We simply pass our savings on to<br>you as we do not profit from our electronic products.<br>You are basically able to <b>"piggy back"</b> on our partner-<br>ships and buying power to get an attractive electronic<br>premium for a fraction of the retail cost.</p>

  <svg class="abs footer-shapes" viewBox="0 1310 1100 114" aria-hidden="true">
    <rect x="0" y="1316" width="410" height="5" fill="#8a8a8a"/>
    <polygon points="0,1321 406,1321 469,1406 1100,1406 1100,1424 0,1424" fill="var(--charcoal)"/>
    <polygon points="410,1316 424,1316 484,1396 1100,1396 1100,1406 469,1406 406,1321" fill="#bfbfbf"/>
  </svg>
  <div class="abs footer-cta">
    <div class="yellow">VIEW ALL THE DETAILS</div>
    <div>OF THIS SPECIAL OFFER AND</div>
    <div>REDEEM ONLINE AT</div>
  </div>
  <div class="abs footer-link">
    <div class="footer-url">WWW.GIFTSANDPERKSHUB.COM</div>
    <div class="footer-terms">*Terms and Conditions apply see website for details</div>
  </div>

</main>
</body>
</html>
```